Business card and stationery for School
Business card and stationery for School - Education
Creative Brief
Use same font as used in my logo
However variations is permitted
Bright & Fun-filled
Mrs Belinda T. Marrowfield
Proprietress
Plot 418C QX4 Temberlo Layout Opposite Pinwick Office Halverton Road, Dosumi FCT, Abuja
info@bluepebbleacademy.example
www.bluepebbleacademy.example

```html
<!DOCTYPE html>
<html lang="en">
<head>
<meta charset="utf-8">
<title>Blue Pebble Academy – Business Card</title>
<link href="https://fonts.googleapis.com/css2?family=Open+Sans:wght@400;600;700&display=swap" rel="stylesheet">
<style>
  :root {
    --stage: #e7e2dc;
    --purple: #8a1f7c;
    --purple-deep: #5e0f55;
    --purple-light: #a13a93;
    --green: #7cae2a;
    --ink: #555555;
    --white: #ffffff;
  }
  * { box-sizing: border-box; margin: 0; padding: 0; }
  html, body {
    width: 1200px; height: 751px; overflow: hidden;
    background: var(--stage);
    font-family: "Open Sans", Arial, sans-serif;
  }
  .canvas { position: relative; width: 1200px; height: 751px; }

  .card {
    position: absolute;
    width: 520px; height: 300px;
    border-radius: 14px;
    overflow: hidden;
    box-shadow: 0 6px 18px rgba(0,0,0,0.18);
  }

  /* Front */
  .card-front { left: 70px; top: 110px; background: var(--white); }
  .card-front .band { position: absolute; left: 0; bottom: 0; width: 520px; height: 110px; }
  .brand {
    position: absolute; left: 30px; top: 132px;
    display: flex; align-items: center; gap: 8px;
    width: 232px;
  }
  .brand-dot { flex: none; width: 20px; height: 20px; border-radius: 50%; background: var(--green); }
  .brand-name {
    font-size: 15px; font-weight: 700; color: var(--purple);
    letter-spacing: 0.3px; text-transform: uppercase; white-space: nowrap;
  }
  .contact { position: absolute; left: 282px; top: 26px; width: 225px; }
  .contact-name { font-size: 16px; font-weight: 700; color: var(--purple); }
  .contact-role { font-size: 11px; color: var(--purple-light); margin-bottom: 16px; }
  .contact-address { font-size: 10.5px; color: var(--ink); line-height: 1.45; margin-bottom: 12px; }
  .contact-line { display: flex; align-items: center; gap: 7px; font-size: 10.5px; color: var(--ink); line-height: 1.6; }
  .contact-line svg { flex: none; }
  .website {
    position: absolute; right: 30px; bottom: 20px;
    font-size: 11px; font-weight: 600; color: var(--white); letter-spacing: 0.6px;
  }

  /* Back */
  .card-back {
    left: 610px; top: 330px;
    background: radial-gradient(circle at 50% 40%, var(--purple-light), var(--purple) 55%, var(--purple-deep));
    display: flex; flex-direction: column; align-items: center; justify-content: center;
    color: var(--white);
  }
  .back-brand { display: flex; align-items: center; gap: 12px; margin-bottom: 26px; }
  .back-brand .brand-dot { background: var(--white); width: 26px; height: 26px; }
  .back-brand .brand-name { color: var(--white); font-size: 26px; }
  .back-tagline { font-size: 13px; letter-spacing: 0.3px; }
</style>
</head>
<body>
<main class="canvas">

  <section class="card card-front" aria-label="Business card front">
    <svg class="band" viewBox="0 0 520 110" aria-hidden="true">
      <path d="M0 62 C140 50 300 48 400 52 L520 40 L520 110 L0 110 Z" fill="#8a1f7c"/>
      <path d="M330 56 L520 40 L520 58 L310 76 Z" fill="#7cae2a"/>
    </svg>

    <div class="brand">
      <span class="brand-dot"></span>
      <span class="brand-name">Blue Pebble Academy</span>
    </div>

    <div class="contact">
      <p class="contact-name">Mrs Belinda T. Marrowfield</p>
      <p class="contact-role">Proprietress</p>
      <p class="contact-address">Plot 418C QX4 Temberlo Layout<br>Opposite Pinwick Office<br>Halverton Road, Dosumi<br>FCT, Abuja</p>
      <p class="contact-line">
        <svg width="10" height="10" viewBox="0 0 10 10" aria-hidden="true"><rect width="10" height="10" fill="#7cae2a"/><path d="M3 2 L4.5 2 L5 4 L4 4.6 Q4.8 6 5.8 6.4 L6.4 5.5 L8 6 L8 7.6 Q4 8 2.4 3 Z" fill="#fff"/></svg>
        +234.805.550.0142
      </p>
      <p class="contact-line">
        <svg width="10" height="10" viewBox="0 0 10 10" aria-hidden="true"><rect width="10" height="10" fill="#7cae2a"/><path d="M3 2 L4.5 2 L5 4 L4 4.6 Q4.8 6 5.8 6.4 L6.4 5.5 L8 6 L8 7.6 Q4 8 2.4 3 Z" fill="#fff"/></svg>
        +234.803.555.0187
      </p>
      <p class="contact-line">
        <svg width="10" height="10" viewBox="0 0 10 10" aria-hidden="true"><rect width="10" height="10" fill="#7cae2a"/><rect x="2" y="3" width="6" height="4" fill="none" stroke="#fff" stroke-width="0.8"/><path d="M2 3 L5 5.3 L8 3" fill="none" stroke="#fff" stroke-width="0.8"/></svg>
        info@bluepebbleacademy.example
      </p>
    </div>

    <p class="website">www.bluepebbleacademy.example</p>
  </section>

  <section class="card card-back" aria-label="Business card back">
    <div class="back-brand">
      <span class="brand-dot"></span>
      <span class="brand-name">Blue Pebble Academy</span>
    </div>
    <p class="back-tagline">"Creche,Nursery &amp; Primary School"</p>
  </section>

</main>
</body>
</html>
```